Web Design

Looking for web designer for total service. We would like to make it in English and Japanese for now. Also need to make Tablet version. Our website is www.brindlecove.com and www.quartzmeadow .com

```html
<!DOCTYPE html>
<html lang="en">
<head>
<meta charset="utf-8">
<title>Quartz Meadow</title>
<link href="https://fonts.googleapis.com/css2?family=Poppins:wght@400;500;600;700&display=swap" rel="stylesheet">
<style>
:root{
  --green:#4e8f31;
  --green-dark:#3f7a26;
  --ink:#111;
  --muted:#555;
  --line:#d9d9d9;
  --black:#0c0c0c;
  --footer:#ececec;
  --white:#fff;
}
*{box-sizing:border-box;margin:0;padding:0}
html,body{width:1200px;height:2927px;overflow:hidden;background:var(--white)}
body{position:relative;font-family:'Poppins',sans-serif;color:var(--ink)}
.abs{position:absolute}

/* header */
.site-header{top:0;left:0;width:1200px;height:94px;background:var(--white)}
.brand{left:146px;top:22px;white-space:nowrap}
.brand-name{font-size:20px;font-weight:600;color:var(--green);line-height:1.2;display:block;white-space:nowrap}
.brand-tag{font-size:11px;color:var(--ink);display:block;margin-top:14px;white-space:nowrap}
.brand-dot{display:inline-block;width:14px;height:14px;border-radius:50%;background:var(--green);vertical-align:middle;margin-right:6px;margin-top:-3px}
.top-contact{right:135px;top:14px;font-size:12px;display:flex;gap:28px;align-items:center}
.top-contact span{display:flex;align-items:center;gap:8px}
.social-square{width:16px;height:16px;background:#3b5998;border-radius:2px}
.main-nav{right:135px;top:56px;display:flex;gap:0;font-size:12.5px;font-weight:500}
.main-nav a{color:var(--ink);text-decoration:none;padding:3px 9px}
.main-nav a.active{background:var(--green);color:var(--white)}

/* hero */
.hero{top:94px;left:0;width:1200px;height:404px;background:linear-gradient(120deg,#2a2a2a 0%,#5b5752 35%,#cfc7b4 55%,#3a3836 80%,#1d1d1d 100%)}
.hero-card{left:133px;top:91px;width:398px;height:205px;background:rgba(78,143,49,.88);color:var(--white);padding:30px 24px}
.hero-card h1{font-size:34px;font-weight:600;line-height:1.1}
.hero-card h2{font-size:25px;font-weight:600;line-height:1.2}
.hero-card p{font-size:13px;line-height:1.35;margin-top:14px}
.hero-arrow{top:178px;width:48px;height:48px}
.hero-dots{top:370px;left:565px;display:flex;gap:8px}
.hero-dots i{width:16px;height:16px;border-radius:50%;background:var(--white);display:block}
.hero-dots i.on{background:var(--green)}

/* about */
.about-photo{left:146px;top:540px;width:307px;height:508px;background:linear-gradient(160deg,#f1f1f1 0%,#c9863a 45%,#d9a04d 70%,#ececec 100%)}
.about-bracket{left:995px;top:562px;width:58px;height:462px;border:10px solid var(--green);border-left:none}
.about-label{left:500px;top:574px;font-size:26px;font-weight:400;display:flex;align-items:center;gap:8px}
.about-label i{display:block;width:44px;height:4px;background:var(--green);margin-top:10px}
.about-title{left:500px;top:600px;font-size:52px;font-weight:600;color:var(--green)}
.about-sub{left:500px;top:658px;font-size:30px;font-weight:400}
.about-lead{left:500px;top:734px;width:480px;font-size:21px;line-height:26.5px}
.about-text{left:500px;top:880px;width:480px;font-size:14.5px;line-height:18px}
.btn-small{left:496px;top:975px;width:74px;height:22px;background:var(--green);color:var(--white);font-size:11px;text-align:center;line-height:22px}

/* services */
.services{top:1128px;left:0;width:1200px;height:527px;background:var(--green)}
.bracket-left{width:16px;border:6px solid var(--white);border-right:none}
.services .bracket-left{left:146px;top:39px;height:121px}
.services-title{left:178px;top:64px;color:var(--white);font-size:34px;font-weight:600}
.services-sub{left:178px;top:104px;color:var(--white);font-size:22px}
.service-card{top:201px;width:293px;height:263px;background:var(--black);overflow:hidden}
.service-img{height:195px;width:100%}
.service-card p{position:absolute;bottom:18px;left:0;width:100%;text-align:center;color:var(--white);font-size:13px;font-weight:600;line-height:1.3}

/* group */
.group-title{top:1700px;left:0;width:1200px;text-align:center;font-size:24px;font-weight:600}
.group-rule{top:1735px;left:568px;width:64px;height:4px;background:var(--green)}
.group-brand{left:152px;top:1779px;width:219px;height:149px;display:flex;align-items:center;justify-content:center;font-size:32px;font-weight:600;color:#1d5c9a;white-space:nowrap}
.group-img{top:1783px;width:211px;height:141px}
.btn-check{left:548px;top:1976px;width:160px;height:38px;background:var(--green);color:var(--white);font-size:16px;font-weight:500;text-align:center;line-height:38px}
.divider{top:2039px;left:131px;width:938px;height:1px;background:var(--line)}

/* contact */
.contact .bracket-left{left:146px;top:2123px;height:156px;border-color:var(--green)}
.contact-heading{left:176px;top:2130px;font-size:36px;font-weight:600;line-height:43px}
.contact-heading em{font-style:normal;color:var(--green)}
.contact-text{left:154px;top:2304px;width:440px;font-size:16px;line-height:20px}
.contact-cta{left:154px;top:2405px;font-size:16px;font-weight:600}
.field{left:613px;width:433px;height:39px;border:1px solid var(--line);font-size:10px;color:#999;padding:12px 14px}
.btn-send{left:613px;top:2390px;width:433px;height:41px;background:var(--green);color:var(--white);font-size:13px;font-weight:500;text-align:center;line-height:41px}

/* partners */
.partners{top:2531px;left:0;width:1200px;height:181px;background:var(--black)}
.partner{top:35px;width:178px;height:117px;background:var(--white);display:flex;align-items:center;justify-content:center;gap:8px;font-size:15px;font-weight:600;color:#222;white-space:nowrap}
.partner i{display:block;width:56px;height:56px;border-radius:50%;flex:none}

/* footer */
.site-footer{top:2712px;left:0;width:1200px;height:215px;background:var(--footer)}
.foot-head{top:37px;font-size:12px;font-weight:600}
.foot-list{top:64px;font-size:11px;line-height:17.5px;color:#333}
.foot-social{top:62px;left:839px;display:flex;gap:9px}
.foot-social i{display:block;width:40px;height:40px;border-radius:50%;background:#2f5f9e}
.foot-rule{top:150px;left:146px;width:907px;height:1px;background:#cfcfcf}
.copyright{top:172px;left:146px;font-size:10.5px;color:#333}
</style>
</head>
<body>

<header class="site-header abs">
  <div class="brand abs">
    <span class="brand-name"><span class="brand-dot"></span>Quartz Meadow</span>
    <span class="brand-tag">Promote monozukuri in Hawaii</span>
  </div>
  <div class="top-contact abs">
    <span>
      <svg width="13" height="13" viewBox="0 0 24 24"><path fill="#4e8f31" d="M6.6 10.8a15 15 0 0 0 6.6 6.6l2.2-2.2a1 1 0 0 1 1-.25 11.4 11.4 0 0 0 3.6.57 1 1 0 0 1 1 1V20a1 1 0 0 1-1 1A17 17 0 0 1 3 4a1 1 0 0 1 1-1h3.5a1 1 0 0 1 1 1c0 1.250.2 2.45.57 3.57a1 1 0 0 1-.25 1z"/></svg>
      (808) 555-0142
    </span>
    <span>
      <svg width="14" height="11" viewBox="0 0 24 18"><rect x="1" y="1" width="22" height="16" fill="none" stroke="#4e8f31" stroke-width="2"/><path d="M1 1l11 9 11-9" fill="none" stroke="#4e8f31" stroke-width="2"/></svg>
      info@quartzmeadow.com
    </span>
    <i class="social-square" role="img" aria-label="Social page link"></i>
  </div>
  <nav class="main-nav abs">
    <a class="active">Home</a><a>Business Contents</a><a>Company Profile</a><a>Suppliers</a><a>Inquiries</a><a>More</a>
  </nav>
</header>

<section class="hero abs" role="img" aria-label="Photo of seasoned rice balls on a dark plate">
  <div class="hero-card abs">
    <h1>Rely on</h1>
    <h2>Businees Expert in Hawaii.</h2>
    <p>Based in Honolulu, Hawaii, based on the concept of "Made in Hawaii", we are working on manufacturing with local companies.</p>
  </div>
  <svg class="hero-arrow abs" style="left:20px" viewBox="0 0 48 48"><path d="M24 2L46 24 24 46 2 24z" fill="none" stroke="#fff" stroke-width="2"/><path d="M28 16l-8 8 8 8" fill="none" stroke="#fff" stroke-width="2.5"/></svg>
  <svg class="hero-arrow abs" style="left:1126px" viewBox="0 0 48 48"><path d="M24 2L46 24 24 46 2 24z" fill="none" stroke="#fff" stroke-width="2"/><path d="M20 16l8 8-8 8" fill="none" stroke="#fff" stroke-width="2.5"/></svg>
  <div class="hero-dots abs"><i class="on"></i><i></i><i></i></div>
</section>

<section class="about">
  <div class="about-photo abs" role="img" aria-label="Photo of honey bottles in a gift box"></div>
  <div class="about-bracket abs"></div>
  <div class="about-label abs">ABOUT US <i></i></div>
  <h2 class="about-title abs">Quartz Meadow</h2>
  <p class="about-sub abs">Promote monozukuri in Hawaii</p>
  <p class="about-lead abs">"Brindle Cove" where premium gourmet items developed by Japanese staff to match the Japanese taste are repeated while repeating trial and error with local companies in Hawaii.</p>
  <p class="about-text abs">Researching high-quality souvenirs and making unique "Made in Hawaii" goods that shape "I hope there is such a product" is popular among souvenirs.</p>
  <div class="btn-small abs">Read more</div>
</section>

<section class="services abs">
  <div class="bracket-left abs"></div>
  <h2 class="services-title abs">What We Do</h2>
  <p class="services-sub abs">Business Contents</p>
  <article class="service-card abs" style="left:146px">
    <div class="service-img" role="img" aria-label="Photo of tropical flowers and jars of Hawaiian food" style="background:linear-gradient(135deg,#7a1d1d,#2f3a2a 60%,#1a1a1a)"></div>
    <p>Planning &amp; manufacturing sales<br>of Hawaiian special food</p>
  </article>
  <article class="service-card abs" style="left:455px">
    <div class="service-img" role="img" aria-label="Photo of a bowl of noodle soup" style="background:radial-gradient(circle at 50% 45%,#e9b25c,#b86a2a 55%,#3a2a1c)"></div>
    <p>Catering Business</p>
  </article>
  <article class="service-card abs" style="left:761px">
    <div class="service-img" role="img" aria-label="Photo of colleagues in a planning meeting" style="background:linear-gradient(135deg,#8fb3c9,#c9b9a4 55%,#4a4f55)"></div>
    <p>New product planning<br>and marketing</p>
  </article>
</section>

<section class="group">
  <h2 class="group-title abs">GROUP COMPANY</h2>
  <div class="group-rule abs"></div>
  <div class="group-brand abs">Brindle Cove</div>
  <div class="group-img abs" style="left:377px;background:linear-gradient(135deg,#6b3a2a,#e2c79a 55%,#9c5a3a)" role="img" aria-label="Photo of pancake mix packages"></div>
  <div class="group-img abs" style="left:603px;background:linear-gradient(135deg,#c9c1b5,#8a6a45 55%,#d8d0c4)" role="img" aria-label="Photo of a coffee stick box"></div>
  <div class="group-img abs" style="left:829px;background:linear-gradient(135deg,#eee,#d79a44 50%,#f2f2f2)" role="img" aria-label="Photo of honey bottles"></div>
  <div class="btn-check abs">CHECK WEBSITE</div>
  <div class="divider abs"></div>
</section>

<section class="contact">
  <div class="bracket-left abs"></div>
  <h2 class="contact-heading abs"><em>Let us help you</em> to<br>find a solution that<br>meets your needs.</h2>
  <p class="contact-text abs">Do you have questions or comments regarding our services? Are you interested in our company or the opportunities we can offer?</p>
  <p class="contact-cta abs">Fill in the form and contact us!</p>
  <div class="field abs" style="top:2127px">Your Name</div>
  <div class="field abs" style="top:2181px">Your Email</div>
  <div class="field abs" style="top:2234px">Contact No.</div>
  <div class="field abs" style="top:2287px;height:86px">Your Email</div>
  <div class="btn-send abs">SEND MESSAGE</div>
</section>

<section class="partners abs">
  <div class="partner abs" style="left:146px"><i style="background:#1a56b0"></i>Palm Mart</div>
  <div class="partner abs" style="left:328px">Nalu Sweets</div>
  <div class="partner abs" style="left:510px" role="img" aria-label="Partner badge"><i style="background:#f2c21b"></i></div>
  <div class="partner abs" style="left:692px;font-size:13px;gap:6px"><i style="background:#7a4b2a;width:40px;height:40px"></i>Kona Ridge Coffee</div>
  <div class="partner abs" style="left:874px" role="img" aria-label="Partner badge"><i style="background:#6a3a8c;border-radius:0;transform:rotate(45deg);width:48px;height:48px"></i></div>
</section>

<footer class="site-footer abs">
  <h3 class="foot-head abs" style="left:146px">CONTACT</h3>
  <p class="foot-list abs" style="left:146px">1450 Kilohana St, Suite 305<br>Honolulu, HI 96817 USA</p>
  <h3 class="foot-head abs" style="left:378px">KEY LINKS</h3>
  <p class="foot-list abs" style="left:378px">Home<br>Business Contents<br>Company Profile</p>
  <p class="foot-list abs" style="left:609px">Suppliers<br>Inquiries<br>More</p>
  <h3 class="foot-head abs" style="left:839px">FOLLOW US</h3>
  <div class="foot-social abs">
    <i role="img" aria-label="Social link"></i><i role="img" aria-label="Social link"></i><i role="img" aria-label="Social link"></i><i role="img" aria-label="Social link"></i>
  </div>
  <div class="foot-rule abs"></div>
  <p class="copyright abs">© All rights reserved, Quartz Meadow, 2018.</p>
</footer>

</body>
</html>
```